Duct Manufacturing Company new to the industry needs business card and stationary design

we are sheet metal duct manufacturers looking for a business card design to fit my new business logo.
nothing to crazy that will date, but want it to stand out from the crowed.
I'm sure you guys will work it out.

Industry/Entity Type

Business

Contact Information for Business Card

Glen Marsh
Director

Address
17 Pollardine St
Tallowbrook NSW 2631

0427 856 143

Sales@flowvane.com.au

Font styles to use
Other font styles liked:
• BankGothic md bt

Requirements
Nice to have
• Like the idea of corner rounded to match logo
• like to keep colours flowing
• font I like sharp square not rounded

```html
<!DOCTYPE html>
<html lang="en">
<head>
<meta charset="utf-8">
<title>Flowvane Industries – Business Card</title>
<link href="https://fonts.googleapis.com/css2?family=Michroma&display=swap" rel="stylesheet">
<style>
  :root {
    --backdrop: #2e3c44;
    --card: #27505f;
    --brand-green: #8cc63f;
    --band-start: #0a5fae;
    --band-end: #0b7fd3;
    --silver: #a7acaf;
    --white: #f4f6f7;
    --muted: #dfe5e8;
  }
  * { box-sizing: border-box; margin: 0; padding: 0; }
  html, body {
    width: 1200px; height: 1200px; overflow: hidden;
    background: var(--backdrop);
    font-family: "Michroma", sans-serif;
  }
  .sheet {
    width: 1200px; height: 1200px;
    display: flex; flex-direction: column; align-items: center; justify-content: center;
    gap: 56px;
  }
  .card {
    position: relative;
    width: 900px; height: 520px;
    background: var(--card);
    border-radius: 14px;
    overflow: hidden;
    box-shadow: 0 14px 30px rgba(0,0,0,.35);
  }

  /* Front */
  .card--front { display: flex; align-items: center; justify-content: center; }
  .brand {
    display: flex; align-items: center; gap: 22px;
    color: var(--brand-green);
    font-size: 40px; letter-spacing: 3px; text-transform: uppercase;
  }
  .brand__dot {
    width: 40px; height: 40px; border-radius: 50%;
    background: var(--brand-green);
    flex: none;
  }
  .brand--stacked { flex-direction: column; gap: 10px; text-align: center; line-height: 1.25; }

  /* Back */
  .card--back .brand {
    position: absolute; left: 70px; top: 150px;
    font-size: 28px; gap: 16px;
  }
  .card--back .brand__dot { width: 30px; height: 30px; }
  .person {
    position: absolute; left: 480px; top: 100px;
    color: var(--white);
  }
  .person__name { font-size: 24px; letter-spacing: 2px; text-transform: uppercase; }
  .person__role { font-size: 14px; letter-spacing: 2px; text-transform: uppercase; margin-top: 8px; color: var(--muted); }
  .person__rule { width: 130px; height: 1px; background: #b9c3c8; margin-top: 46px; }
  .contacts {
    position: absolute; left: 480px; top: 258px;
    list-style: none; color: var(--white);
    font-size: 14px; letter-spacing: 2px; text-transform: uppercase;
  }
  .contacts li { display: flex; align-items: center; gap: 14px; height: 36px; }
  .contacts svg { width: 20px; height: 20px; flex: none; fill: none; stroke: var(--white); stroke-width: 1.6; }
  .contacts .icon-phone { fill: var(--white); stroke: none; }

  .footer-band {
    position: absolute; left: 0; bottom: 0;
    width: 900px; height: 118px;
    background: linear-gradient(90deg, var(--band-start), var(--band-end));
    border-top: 6px solid var(--silver);
  }
  .address {
    position: absolute; left: 100px; top: 420px;
    color: var(--white); font-size: 17px; letter-spacing: 3px; line-height: 1.95;
    text-transform: uppercase;
  }
</style>
</head>
<body>
<main class="sheet">
  <section class="card card--front" aria-label="Business card front">
    <div class="brand brand--stacked">
      <span class="brand__dot"></span>
      <span>Flowvane<br>Industries</span>
    </div>
  </section>

  <section class="card card--back" aria-label="Business card back">
    <div class="footer-band" role="img" aria-label="Blue footer band with a silver edge"></div>

    <div class="brand">
      <span class="brand__dot"></span>
      <span>Flowvane</span>
    </div>

    <div class="person">
      <p class="person__name">Glen Marsh</p>
      <p class="person__role">Director</p>
      <div class="person__rule"></div>
    </div>

    <ul class="contacts">
      <li>
        <svg viewBox="0 0 20 20"><path class="icon-phone" d="M3 7c0-3 3-4 7-4s7 1 7 4l-3 1-1-2H7L6 8 3 7Zm3 2h8l3 7H3l3-7Zm4 1.5a2.2 2.2 0 1 0 0 4.4 2.2 2.2 0 0 0 0-4.4Z"/></svg>
        <span>0427 856 143</span>
      </li>
      <li>
        <svg viewBox="0 0 20 20"><rect x="2" y="4.5" width="16" height="11"/><path d="M2 4.5l8 6 8-6M2 15.5l6-5M18 15.5l-6-5"/></svg>
        <span>Sales@flowvane.com.au</span>
      </li>
      <li>
        <svg viewBox="0 0 20 20"><circle cx="10" cy="10" r="8"/><ellipse cx="10" cy="10" rx="3.5" ry="8"/><path d="M2 10h16M3.5 6h13M3.5 14h13"/></svg>
        <span>www.flowvane.com.au</span>
      </li>
    </ul>

    <p class="address">17 Pollardine St<br>Tallowbrook NSW 2631</p>
  </section>
</main>
</body>
</html>
```